Label designs for a new company manufacturing food supplements bottles and containers

The design must reflect SPIRITUAL as well as PHYSICAL THERAPEUTIC BENEFITS ,Our company BRIGHTWATER HERBALIST produces Food Supplements products line. Such as vitamins, herbs, super foods,alkalizing , weight loss and amino acids these products are made of , pills, capsules, powders and liquids. The containers are of different sizes , small , medium and large . We need a contemporary label design that represents alternative approaches to physical and spiritual healing . Labels should exude trust worthiness, character, and quality to achieve optimum customer confidence.

Target Market(s)

People of age 25 & up , 50% female 50% Male

Industry/Entity Type

Alternative Medicine

Font styles to use
Serif

Requirements
Must have
• name of company, name of product , slogan or short description for people to understand what the product is all about . supplement facts, ingredient list, directions, statements , place of production, expiration and lot numbers.
Nice to have
• Easily recognizable corporate identity for optimum brand identification.
Should not have
• Playfulness

```html
<!DOCTYPE html>
<html lang="en">
<head>
<meta charset="utf-8">
<title>Brightwater Herbalist – Leniva Label</title>
<link rel="stylesheet" href="https://fonts.googleapis.com/css2?family=Noto+Sans:ital,wght@0,400;0,700;1,400&display=swap">
<style>
  :root {
    --stage: #e3e4e5;
    --leaf-green: #80b42b;
    --teal: #31aa88;
    --brand-blue: #25679a;
    --product-pink: #d6509a;
    --table-frame: #6f77b9;
    --ink: #111;
    --white: #fff;
    --swatch-blue: #a9dbf2;
    --swatch-yellow: #f9ef2a;
  }
  * { box-sizing: border-box; margin: 0; padding: 0; }
  html, body { width: 1200px; height: 844px; overflow: hidden; }
  body { background: var(--stage); font-family: "Noto Sans", sans-serif; color: var(--ink); position: relative; }

  .label {
    position: absolute; left: 124px; top: 214px;
    width: 1016px; height: 413px;
    transform: scale(0.937); transform-origin: 0 0;
    overflow: hidden;
    background: linear-gradient(90deg,
      var(--leaf-green) 0%, var(--leaf-green) 9%,
      #e4eecd 30%, var(--white) 45%, var(--white) 66%,
      #e4eecd 76%, var(--leaf-green) 90%, var(--leaf-green) 100%);
  }
  .label__band { position: absolute; left: 0; top: 0; width: 1016px; height: 413px; }
  .abs { position: absolute; }

  .section-title { color: var(--white); font-weight: 700; font-size: 15px; letter-spacing: .6px; }
  .indications__title { left: 18px; top: 36px; }
  .indications__text { left: 18px; top: 56px; width: 293px; font-style: italic; font-size: 14.8px; line-height: 17px; }
  .usage__title { left: 18px; top: 138px; }
  .usage__text { left: 18px; top: 158px; width: 292px; font-size: 12.6px; line-height: 15.3px; text-align: justify; }

  .brand-mark { left: 469px; top: 31px; width: 76px; height: 76px; border-radius: 50%; background: var(--brand-blue); }
  .brand-name { left: 258px; top: 106px; width: 500px; text-align: center; font-size: 31px; line-height: 40px; color: var(--brand-blue); }
  .tagline { left: 258px; top: 152px; width: 500px; text-align: center; font-size: 19px; line-height: 24px; color: var(--brand-blue); }
  .product-name { left: 258px; top: 188px; width: 500px; text-align: center; font-weight: 700; font-size: 62px; letter-spacing: 1px; color: var(--product-pink); line-height: 1.1; }
  .product-claim { left: 258px; top: 254px; width: 500px; text-align: center; font-weight: 700; font-size: 17px; letter-spacing: .8px; color: var(--brand-blue); }

  .formula-title { left: 706px; top: 32px; font-weight: 700; font-size: 13.5px; }
  .facts { left: 706px; top: 58px; width: 297px; height: 185px; background: var(--white); border: 2px solid var(--table-frame); border-radius: 14px; }
  .facts__head { position: absolute; left: 10px; font-weight: 700; font-size: 14px; color: var(--teal); }
  .facts__text { position: absolute; font-size: 14px; }
  .facts__rule { position: absolute; left: 0; width: 289px; height: 2px; background: var(--table-frame); }
  .facts__small { position: absolute; left: 10px; top: 162px; font-size: 10px; }
  .ingredients { position: absolute; left: 10px; top: 89px; font-size: 13.5px; line-height: 16px; list-style: none; }

  .swatch { width: 54px; height: 54px; border-radius: 50%; border: 3px solid var(--teal); }
  .swatch--blue { left: 735px; top: 267px; background: var(--swatch-blue); }
  .swatch--yellow { left: 808px; top: 263px; background: var(--swatch-yellow); }
  .swatch--white { left: 877px; top: 251px; background: var(--white); }

  .lot-box { left: 17px; top: 304px; width: 151px; height: 37px; border: 1px solid #1f5f4c; font-size: 8.8px; line-height: 10.4px; padding: 2px 5px; }
  .origin-note { left: 19px; top: 347px; font-size: 11px; line-height: 15px; color: var(--white); }
  .supplement-line { left: 308px; top: 352px; width: 400px; text-align: center; font-size: 15px; line-height: 19px; color: var(--white); }
  .statement { left: 716px; top: 324px; width: 135px; font-size: 11.3px; line-height: 14px; }
</style>
</head>
<body>
  <main class="label" aria-label="Leniva supplement bottle label">
    <svg class="label__band" viewBox="0 0 1016 413" aria-hidden="true">
      <path d="M0 258 Q508 366 1016 256 L1016 413 L0 413 Z" fill="var(--teal)"/>
    </svg>

    <h2 class="abs section-title indications__title">INDICATIONS:</h2>
    <p class="abs indications__text">Lorem ipsum dolor sit amet, consectetur adipisci elit, sed eiusmod tempor incidunt ut labore et dolore magna aliqua.</p>

    <h2 class="abs section-title usage__title">USAGE:</h2>
    <p class="abs usage__text">Quis aute iure reprehenderit in voluptate velit esse cillum dolore eu fugiat nulla pariatur. Excepteur sint obcaecat cupiditat non proident, sunt in culpa qui officia deserunt mollit anim id est laborum.</p>

    <div class="abs brand-mark" aria-hidden="true"></div>
    <p class="abs brand-name">Brightwater Herbalist</p>
    <p class="abs tagline">Rooted in Care</p>
    <h1 class="abs product-name">LENIVA</h1>
    <p class="abs product-claim">CONSTIPATION SUPPORT</p>

    <p class="abs formula-title">Dr Halvern Original Proprietary Formula</p>
    <section class="abs facts" aria-label="Supplement facts">
      <p class="facts__head" style="top:7px">Lorem ipsum dolor sit amet</p>
      <p class="facts__text" style="left:10px;top:24px">Lorem ipsum dolor sit amet</p>
      <div class="facts__rule" style="top:51px"></div>
      <p class="facts__head" style="top:56px">Lorem ipsum dolor</p>
      <p class="facts__text" style="right:6px;top:56px">%Daily Value</p>
      <div class="facts__rule" style="top:78px"></div>
      <ul class="ingredients">
        <li>Cascara sagrada..............................”</li>
        <li>Aloe Vera.........................................”</li>
        <li>Fennel seed ....................................”</li>
      </ul>
      <div class="facts__rule" style="top:155px"></div>
      <p class="facts__small">Lorem ipsum dolor sit amet</p>
    </section>

    <div class="abs swatch swatch--blue" aria-hidden="true"></div>
    <div class="abs swatch swatch--yellow" aria-hidden="true"></div>
    <div class="abs swatch swatch--white" aria-hidden="true"></div>

    <p class="abs lot-box">Lorem ipsum dolor sit amet,<br>consectetur adipisci elit,<br>sed eiusmod tempor incidunt.</p>
    <p class="abs origin-note">Lorem ipsum dolor sit amet,<br>consectetur adipisci elit,<br>sed eiusmod tempor incidunt.</p>
    <p class="abs supplement-line">DIETARY SUPPLEMENT<br>60 caps - 1000 mg</p>
    <p class="abs statement">Lorem ipsum dolor sit amet, consectetur adipisci elit,<br>sed eiusmod tempor incidunt.</p>
  </main>
</body>
</html>
```